Business cards design on a high standard

We advise clients on insurance and financial matters, since these clients pay for our advice, the design should have a high standard. Our logo should be included. From the colors we are open for everything.

Colors

Designer to choose colors to be used in the design.

```html
<!DOCTYPE html>
<html lang="en">
<head>
<meta charset="utf-8">
<title>Alpine Counsel – Business Cards</title>
<link rel="stylesheet" href="https://fonts.googleapis.com/css2?family=Gabriela&family=Michroma&family=Arimo:wght@400&display=swap">
<style>
  :root {
    --page: #ffffff;
    --red: #e3222a;
    --ink: #111111;
    --grey: #8a8a8a;
    --grey-dark: #6e6e6e;
    --text-grey: #5a5a5a;
    --card-white: #ffffff;
  }
  html, body {
    margin: 0;
    padding: 0;
    width: 1200px;
    height: 1200px;
    overflow: hidden;
    background: var(--page);
  }
  .canvas {
    position: relative;
    width: 1200px;
    height: 1200px;
  }
  .card {
    position: absolute;
    width: 349px;
    height: 551px;
  }
  .card-bg {
    position: absolute;
    inset: 0;
    width: 100%;
    height: 100%;
  }
  .card--front { left: 227px; top: 340px; }
  .card--back { left: 595px; top: 333px; }

  /* Front */
  .holder {
    position: absolute;
    right: 62px;
    top: 58px;
    text-align: right;
  }
  .holder-name {
    font-family: "Gabriela", serif;
    color: var(--red);
    font-size: 37px;
    line-height: 1;
    margin: 0;
  }
  .holder-role {
    font-family: "Gabriela", serif;
    color: var(--text-grey);
    font-size: 13px;
    margin-top: 6px;
  }
  .holder-line {
    font-family: "Gabriela", serif;
    color: var(--text-grey);
    font-size: 9.5px;
    margin-top: 1px;
  }
  .holder-address {
    font-family: "Arimo", sans-serif;
    color: var(--text-grey);
    font-size: 11.5px;
    line-height: 1.4;
    margin-top: 6px;
    letter-spacing: 0.3px;
  }
  .brand-front {
    position: absolute;
    left: 0;
    right: 0;
    top: 242px;
    text-align: center;
    font-family: "Michroma", sans-serif;
    color: var(--red);
    line-height: 1.05;
  }
  .brand-front .brand-main { font-size: 40px; letter-spacing: 1px; }
  .brand-front .brand-sub { font-size: 19px; letter-spacing: 5px; }
  .socials {
    position: absolute;
    left: 122px;
    top: 375px;
    display: flex;
    gap: 6px;
  }
  .social-square {
    width: 21px;
    height: 21px;
    border-radius: 3px;
    background: var(--grey-dark);
  }
  .contacts {
    position: absolute;
    left: 119px;
    top: 414px;
    list-style: none;
    margin: 0;
    padding: 0;
  }
  .contact {
    display: flex;
    align-items: center;
    height: 26px;
    margin-bottom: 10px;
    font-family: "Arimo", sans-serif;
    font-size: 13px;
    color: var(--text-grey);
    letter-spacing: 0.3px;
  }
  .contact-icon {
    width: 26px;
    height: 26px;
    margin-right: 14px;
  }

  /* Back */
  .back-lockup {
    position: absolute;
    left: 174px;
    top: 290px;
    width: 380px;
    transform: translate(-50%, -50%) rotate(-90deg);
    text-align: center;
  }
  .brand-back {
    font-family: "Michroma", sans-serif;
    color: var(--red);
    line-height: 1.05;
  }
  .brand-back .brand-main { font-size: 54px; letter-spacing: 1px; }
  .brand-back .brand-sub { font-size: 27px; letter-spacing: 7px; }
  .back-tagline {
    font-family: "Gabriela", serif;
    color: var(--red);
    font-size: 19px;
    margin-top: 6px;
  }
</style>
</head>
<body>
<main class="canvas">

  <section class="card card--front" aria-label="Business card front">
    <svg class="card-bg" viewBox="0 0 349 551" aria-hidden="true">
      <path d="M40 0 H349 V531 Q349 551 329 551 H0 V40 Q0 0 40 0 Z" fill="var(--ink)"/>
      <path d="M40 0 H250 C318 50 349 170 349 270 V531 Q349 551 329 551 H84 C32 480 0 380 0 290 V40 Q0 0 40 0 Z" fill="var(--card-white)"/>
      <path d="M262 0 C318 42 342 100 349 150" fill="none" stroke="var(--red)" stroke-width="3"/>
    </svg>

    <div class="holder">
      <h1 class="holder-name">Marten Keller</h1>
      <div class="holder-role">Advisor</div>
      <div class="holder-line">Insurance and financial matters</div>
      <div class="holder-address">Address: P.O. Box 4210<br>Riverton, Wyoming 56118</div>
    </div>

    <div class="brand-front">
      <div class="brand-main">ALPINE</div>
      <div class="brand-sub">COUNSEL</div>
    </div>

    <div class="socials" aria-hidden="true">
      <span class="social-square"></span>
      <span class="social-square"></span>
      <span class="social-square"></span>
    </div>

    <ul class="contacts">
      <li class="contact">
        <svg class="contact-icon" viewBox="0 0 26 26" aria-hidden="true">
          <circle cx="13" cy="13" r="12" fill="#e6e6e6" stroke="#bdbdbd"/>
          <rect x="9.5" y="6" width="7" height="14" rx="1.5" fill="#555"/>
          <rect x="10.8" y="8" width="4.4" height="5" fill="#e6e6e6"/>
        </svg>
        307-555-0142
      </li>
      <li class="contact">
        <svg class="contact-icon" viewBox="0 0 26 26" aria-hidden="true">
          <circle cx="13" cy="13" r="12" fill="#e6e6e6" stroke="#bdbdbd"/>
          <rect x="7" y="9" width="12" height="8.5" fill="none" stroke="#555" stroke-width="1.5"/>
          <path d="M7 9 L13 14 L19 9" fill="none" stroke="#555" stroke-width="1.5"/>
        </svg>
        info@alpinecounsel.com
      </li>
      <li class="contact">
        <svg class="contact-icon" viewBox="0 0 26 26" aria-hidden="true">
          <circle cx="13" cy="13" r="12" fill="#e6e6e6" stroke="#bdbdbd"/>
          <circle cx="13" cy="13" r="6" fill="none" stroke="#555" stroke-width="1.4"/>
          <ellipse cx="13" cy="13" rx="2.6" ry="6" fill="none" stroke="#555" stroke-width="1.2"/>
          <line x1="7" y1="13" x2="19" y2="13" stroke="#555" stroke-width="1.2"/>
        </svg>
        www.alpinecounsel.com
      </li>
    </ul>
  </section>

  <section class="card card--back" aria-label="Business card back">
    <svg class="card-bg" viewBox="0 0 349 551" aria-hidden="true">
      <defs>
        <linearGradient id="backGrey" x1="0" y1="0" x2="1" y2="1">
          <stop offset="0" stop-color="#a8a8a8"/>
          <stop offset="1" stop-color="#7c7c7c"/>
        </linearGradient>
      </defs>
      <path d="M40 0 H349 V511 Q349 551 309 551 H0 V40 Q0 0 40 0 Z" fill="url(#backGrey)"/>
      <path d="M40 0 H150 C290 20 349 140 349 300 V511 Q349 551 309 551 H40 Q0 551 0 511 V300 C20 120 0 0 40 0 Z" fill="var(--card-white)"/>
      <path d="M190 4 C280 30 330 100 349 190" fill="none" stroke="#b5b5b5" stroke-width="8"/>
    </svg>

    <div class="back-lockup">
      <div class="brand-back">
        <div class="brand-main">ALPINE</div>
        <div class="brand-sub">COUNSEL</div>
      </div>
      <div class="back-tagline">Insurance and financial matters</div>
    </div>
  </section>

</main>
</body>
</html>
```